Maple. Crest PT Tri-Fold

An on demand house call mobile physical therapy and wellness company. Focused on quality rehabilitation management health and wellness needs to your door.
We need a tri-fold brochure to describe our services

Target Market(s)

Patients in need of physical therapy

Industry/Entity Type

Physical Therapy

Font styles to use
Serif
Sans Serif
Other font styles liked:
• Attached is some necessary content from a prior brochure

Colors
0054AA
0677BA
7BADD7
CADEEF
E8F1F8
EB3D1F
EC4F4E
F09395
F8D3D4
FCEDEE

```html
<!DOCTYPE html>
<html lang="en">
<head>
<meta charset="utf-8">
<title>Maple. Crest PT Tri-Fold</title>
<link href="https://fonts.googleapis.com/css2?family=Montserrat:ital,wght@0,300;0,400;0,500;0,600;0,700;0,800;1,300;1,400&display=swap" rel="stylesheet">
<style>
  :root {
    --blue-deep: #0054AA;
    --blue-mid: #0677BA;
    --blue-soft: #7BADD7;
    --blue-pale: #CADEEF;
    --blue-mist: #E8F1F8;
    --red-bright: #EB3D1F;
    --red-main: #EC4F4E;
    --red-soft: #F09395;
    --red-pale: #F8D3D4;
    --red-mist: #FCEDEE;
    --list-blue: #5f8dc8;
    --title-blue: #6f9fd3;
    --paper: #f3f3f3;
    --backdrop: #e4e4e4;
    --white: #ffffff;
  }
  * { box-sizing: border-box; margin: 0; padding: 0; }
  html, body {
    width: 1200px; height: 675px; overflow: hidden;
    background: var(--backdrop);
    font-family: 'Montserrat', sans-serif;
  }
  .brochure {
    position: absolute; left: 180px; top: 22px;
    width: 840px; height: 630px;
    display: flex;
    box-shadow: 0 8px 28px rgba(0,0,0,0.18);
  }
  .panel { position: relative; width: 280px; height: 630px; overflow: hidden; }

  /* Left panel */
  .panel-intro {
    background: var(--red-main);
    color: var(--white);
    text-align: center;
    padding: 44px 26px 0;
  }
  .brand-name {
    font-weight: 600; font-size: 24px; letter-spacing: 0.2px;
    margin-top: 40px;
  }
  .tagline {
    font-style: italic; font-weight: 300; font-size: 17px; line-height: 1.5;
    letter-spacing: 0.6px;
  }
  .tagline-first { margin-top: 28px; }
  .divider { height: 1px; background: var(--white); margin: 12px 4px 14px; opacity: 0.9; }
  .intro-body {
    margin-top: 46px;
    text-align: justify; text-align-last: left;
    font-size: 12.5px; line-height: 2.05; letter-spacing: 0.6px; font-weight: 400;
    padding: 0 2px;
  }

  /* Middle panel */
  .panel-benefits {
    background: var(--red-main);
    color: var(--white);
    border-left: 1px solid rgba(255,255,255,0.18);
  }
  .photo-area {
    position: absolute; left: 0; top: 0; width: 280px; height: 310px;
    background:
      radial-gradient(ellipse at 55% 45%, rgba(245,160,160,0.55), transparent 60%),
      linear-gradient(180deg, #d9484a 0%, #e66a68 55%, var(--red-main) 100%);
  }
  .benefit-list {
    position: absolute; left: 22px; right: 14px; top: 322px;
    list-style: none;
    font-size: 10.2px; line-height: 1.36; letter-spacing: 0.3px; font-weight: 400;
  }
  .benefit-list li { position: relative; padding-left: 12px; margin-bottom: 6px; }
  .benefit-list li::before {
    content: ""; position: absolute; left: 0; top: 6px;
    width: 3px; height: 3px; border-radius: 50%; background: var(--white);
  }

  /* Right panel */
  .panel-programs { background: var(--paper); }
  .illustration {
    position: absolute; left: 38px; width: 100px; height: 78px;
    border-radius: 6px;
    background: linear-gradient(160deg, var(--blue-mist), var(--blue-pale));
  }
  .illustration-one { top: 34px; }
  .illustration-two { top: 132px; }
  .illustration-three { top: 230px; }
  .programs-title {
    position: absolute; left: 170px; top: 322px;
    width: 306px; height: 102px;
    transform-origin: top left;
    transform: rotate(-90deg);
    text-align: right;
    color: var(--blue-soft);
    line-height: 1;
    white-space: nowrap;
  }
  .programs-title .title-light {
    display: block; font-weight: 300; font-size: 36px; letter-spacing: 0.5px;
    line-height: 42px;
  }
  .programs-title .title-bold {
    display: block; font-weight: 800; font-size: 52px; letter-spacing: -1px;
    color: var(--title-blue); line-height: 58px;
  }
  .program-list {
    position: absolute; left: 24px; right: 24px; top: 336px;
    list-style: none; text-align: center;
    color: var(--list-blue);
    font-weight: 500; font-size: 12.5px; letter-spacing: 2.4px;
    text-transform: uppercase;
  }
  .program-list li {
    padding: 5px 0 4px;
    border-bottom: 1px solid var(--list-blue);
    line-height: 1.2;
  }
  .program-list li:last-child { border-bottom: none; }
</style>
</head>
<body>
  <div class="brochure">
    <section class="panel panel-intro">
      <h1 class="brand-name">Maple. Crest PT</h1>
      <p class="tagline tagline-first">Physical therapy,<br>delivered to you</p>
      <div class="divider"></div>
      <p class="tagline">Finding the right<br>rehabilitation setting<br>shapes recovery</p>
      <div class="divider"></div>
      <p class="tagline">Convenient support<br>and expert therapist</p>
      <p class="intro-body">Our home-based outpatient physical therapy delivers high quality therapy services in the comfort of your own home. Patients are not required to be “homebound,” as they would in the home health setting.</p>
    </section>

    <section class="panel panel-benefits">
      <div class="photo-area" role="img" aria-label="Photo of a therapist stretching a patient's leg on a living room floor, tinted red"></div>
      <ul class="benefit-list">
        <li>Not having to arrange for someone to drive them to a clinic</li>
        <li>The privacy that comes from one-on-one care</li>
        <li>Building a treatment plan around how they live</li>
        <li>The use of the home to provide space for exercise in order to build commitment to a home exercise plan</li>
        <li>The sense of independence gained from getting better and gaining function in the home</li>
        <li>The sense of family that comes from knowing you have a skilled clinician who knows the ins and outs of your home and your loved one’s challenges and can be reached when you need them.</li>
      </ul>
    </section>

    <section class="panel panel-programs">
      <div class="illustration illustration-one" role="img" aria-label="Illustration of a therapist treating a patient lying on a mat"></div>
      <div class="illustration illustration-two" role="img" aria-label="Illustration of a therapist stretching a patient's arm on a table"></div>
      <div class="illustration illustration-three" role="img" aria-label="Illustration of a therapist massaging a patient's back on a table"></div>
      <h2 class="programs-title">
        <span class="title-light">Rehabilitation</span>
        <span class="title-bold">Programs</span>
      </h2>
      <ul class="program-list">
        <li>Geriatrics</li>
        <li>Neurological</li>
        <li>Orthopedics</li>
        <li>Post-operative</li>
        <li>Sports medicine</li>
        <li>Balance/vestibular</li>
        <li>CHF</li>
        <li>COPD</li>
        <li>Home safety and<br>fall prevention</li>
      </ul>
    </section>
  </div>
</body>
</html>
```